Harborline Talent IT Recruiting firm needs a business card design for Recruiters, Sourcers, and Account

We need business cards that allow us to change all contact info, names, titles (Recruiter, Sourcer, Account Manager, Director, CEO, etc) per person since we have three offices, in three cities, Phoenix, Austin, and Las Vegas. We do recruiting and contractors for IT positions (Developers, Architects, Software Engineers, Security Engineers, Help Desk, DBAs, PMs, Scrum Masters, etc.) Our client companies are very diverse from Crestline 250 to silicone Valley type start-ups.

So, while we what hip, techie, and quirky, it still needs to be professional. Primary color we use is blue, with silver as a secondary color.

Target Market(s)

IT, Technology

Industry/Entity Type

Business

Contact Information for Business Card

Company name: Harborline Talent, Inc.
Website: www.harborlinetalent-example.com
Logos for ProCircle, Quillo, and Roomwall

Name, Title, Office Number, Cell Number, email

Font styles to use
Serif
Sans Serif

Colors
0455a3
d5d5d5

Requirements
Nice to have
• The grey I selected below is not necessary - but, would like silver included. I included a card design (File 3: HTI early trial example.jpg) that I had started on. It's very rough, and not quite what we're looking for, but what we did like is the logo, big, maybe a bit faded, off center, goes out of frame, etc. Still looking for other ideas - you are the pros! But, just an idea of a design element we liked.

```html
<!DOCTYPE html>
<html lang="en">
<head>
<meta charset="utf-8">
<title>Harborline Talent — Business Card</title>
<link rel="stylesheet" href="https://fonts.googleapis.com/css2?family=Arimo:wght@400;700&family=Cinzel:wght@400&display=swap">
<style>
  :root {
    --stage: #2b2b2b;
    --navy: #2b2a7f;
    --band: #e4e4e6;
    --brand-blue: #1f8fd6;
    --ink: #1e1e24;
    --silver-light: #ffffff;
    --silver-dark: #d9d9dc;
    --faded-blue: #62b3e3;
  }
  * { box-sizing: border-box; margin: 0; padding: 0; }
  html, body { width: 1200px; height: 878px; overflow: hidden; }
  body {
    background: var(--stage);
    font-family: "Arimo", Arial, sans-serif;
    position: relative;
  }
  .card {
    position: absolute;
    width: 525px;
    height: 300px;
    border-radius: 14px;
    overflow: hidden;
  }
  /* ---------- Back side ---------- */
  .card-back {
    left: 50px; top: 289px;
    background: var(--navy);
  }
  .card-back .band {
    position: absolute;
    left: 0; right: 0; top: 38px; height: 226px;
    background: var(--band);
    text-align: center;
  }
  .wordmark {
    font-family: "Cinzel", Georgia, serif;
    font-weight: 400;
    color: var(--ink);
    letter-spacing: 2px;
    white-space: nowrap;
  }
  .card-back .wordmark { font-size: 30px; margin-top: 20px; }
  .tagline {
    font-family: "Cinzel", Georgia, serif;
    color: var(--ink);
    letter-spacing: 2.5px;
    white-space: nowrap;
  }
  .card-back .tagline { font-size: 10px; margin-top: 10px; }
  .community {
    color: var(--brand-blue);
    font-size: 17px;
    margin-top: 16px;
  }
  .socials {
    display: flex;
    justify-content: space-around;
    margin: 14px 20px 0;
  }
  .social {
    display: flex;
    flex-direction: column;
    align-items: center;
    gap: 5px;
    color: var(--brand-blue);
    font-size: 11px;
    white-space: nowrap;
  }
  .social .dot {
    width: 10px; height: 10px;
    border-radius: 50%;
    background: var(--navy);
  }
  .website {
    color: var(--brand-blue);
    font-size: 17px;
    margin-top: 22px;
  }
  /* ---------- Front side ---------- */
  .card-front {
    left: 625px; top: 289px;
    background: linear-gradient(160deg, var(--silver-light) 0%, #f1f1f2 55%, var(--silver-dark) 100%);
  }
  .card-front .brand {
    position: absolute;
    right: 24px; top: 22px;
    text-align: right;
  }
  .card-front .wordmark { font-size: 22px; }
  .card-front .tagline { font-size: 8.5px; margin-top: 6px; }
  .divider {
    position: absolute;
    left: 24px; right: 24px; top: 116px;
    height: 2px;
    background: var(--ink);
  }
  .emblem-fade {
    position: absolute;
    right: -42px; top: 170px;
    width: 140px; height: 140px;
    border-radius: 50%;
    background: var(--faded-blue);
    opacity: .75;
  }
  .person {
    position: absolute;
    left: 24px; top: 158px;
    width: 300px;
  }
  .person .name {
    color: var(--brand-blue);
    font-size: 18px;
  }
  .person .title-row {
    display: flex;
    align-items: center;
    gap: 6px;
    margin-top: 3px;
  }
  .person .title {
    color: var(--ink);
    font-size: 12px;
  }
  .person .title-row .rule {
    flex: 1;
    height: 2px;
    background: var(--ink);
  }
  .contacts {
    list-style: none;
    margin-top: 8px;
  }
  .contacts li {
    display: flex;
    align-items: center;
    gap: 8px;
    color: var(--brand-blue);
    font-size: 11.5px;
    height: 20px;
    white-space: nowrap;
  }
  .contacts svg { width: 14px; height: 14px; flex: none; }
</style>
</head>
<body>

  <section class="card card-back" aria-label="Business card, back">
    <div class="band">
      <div class="wordmark">HARBORLINE TALENT</div>
      <div class="tagline">STEERING TALENT FORWARD</div>
      <div class="community">Join our community</div>
      <div class="socials">
        <div class="social" aria-label="ProCircle"><span class="dot"></span>Harborline Talent</div>
        <div class="social" aria-label="Roomwall"><span class="dot"></span>Harborline Talent</div>
        <div class="social" aria-label="Quillo"><span class="dot"></span>@HarborlineTalent</div>
        <div class="social" aria-label="Plusfold"><span class="dot"></span>Harborline Talent</div>
      </div>
      <div class="website">www.harborlinetalent-example.com</div>
    </div>
  </section>

  <section class="card card-front" aria-label="Business card, front">
    <div class="brand">
      <div class="wordmark">HARBORLINE TALENT</div>
      <div class="tagline">STEERING TALENT FORWARD</div>
    </div>
    <div class="divider"></div>
    <div class="emblem-fade" role="img" aria-label="Large faded brand emblem running off the card edge"></div>

    <div class="person">
      <div class="name">Dana Whitfield</div>
      <div class="title-row"><span class="title">CEO</span><span class="rule"></span></div>
      <ul class="contacts">
        <li>
          <svg viewBox="0 0 16 16" aria-hidden="true"><path d="M2 5c0-2 3-3 6-3s6 1 6 3v1h-3V4.5H5V6H2z M4 7h8l1.5 6h-11z" fill="#1e1e24"/></svg>
          602 | 555-0143
        </li>
        <li>
          <svg viewBox="0 0 16 16" aria-hidden="true"><rect x="3.5" y="1" width="9" height="14" rx="1.5" fill="none" stroke="#1e1e24" stroke-width="1.3"/><line x1="6.5" y1="13" x2="9.5" y2="13" stroke="#1e1e24" stroke-width="1"/></svg>
          512-555-0187
        </li>
        <li>
          <svg viewBox="0 0 16 16" aria-hidden="true"><rect x="1" y="3" width="14" height="10" fill="none" stroke="#1e1e24" stroke-width="1.2"/><path d="M1 3l7 6 7-6" fill="none" stroke="#1e1e24" stroke-width="1.2"/></svg>
          ----@harborlinetalent-example.com
        </li>
      </ul>
    </div>
  </section>

</body>
</html>
```